Flyer Design Project

Training and Consulting Flyer

I attached a document that contained the wording for the flyer as well as the logo.

Target Market(s)

Willow Crest agencies and grantees

Industry/Entity Type

Training

Font styles to use
Sans Serif

Colors
e667a6
eda3c7
a54499
b768aa
f9d9e8

Requirements
Must have
• Words provided on attachment
Nice to have
• Graphics that are related to adult training/learning and consulting

```html
<!DOCTYPE html>
<html lang="en">
<head>
<meta charset="utf-8">
<title>Ardea Health Consultants – Flyer</title>
<link rel="stylesheet" href="https://fonts.googleapis.com/css2?family=Bebas+Neue&family=Open+Sans:ital,wght@0,400;0,600;0,700;1,400;1,700&display=swap">
<style>
  :root{
    --backdrop:#3d3d3d;
    --paper:#ffffff;
    --magenta:#b21f74;
    --ink:#1c1c1c;
    --muted:#555555;
    --footer:#222222;
    --photo-people:#b7a9a4;
    --photo-juice:#c9573a;
    --photo-kitchen:#d9c8bd;
  }
  *{box-sizing:border-box;margin:0;padding:0}
  html,body{width:1200px;height:1200px;overflow:hidden;background:var(--backdrop)}
  .flyer{position:absolute;left:194px;top:76px;width:812px;height:1050px;background:var(--paper);overflow:hidden;box-shadow:0 4px 18px rgba(0,0,0,.45)}
  .side-sweep{position:absolute;left:0;top:0;width:812px;height:1050px}

  .brand{position:absolute;left:38px;top:52px;width:210px}
  .brand-row{display:flex;align-items:center;gap:12px}
  .brand-dot{width:34px;height:34px;border-radius:50%;background:var(--magenta);flex:none}
  .brand-name{font-family:"Open Sans",sans-serif;font-weight:700;font-size:19px;line-height:24px;color:var(--ink)}
  .brand-tagline{font-family:"Open Sans",sans-serif;font-size:12px;color:var(--muted);margin-top:14px;letter-spacing:.4px}

  .pillars{position:absolute;left:38px;top:164px;width:207px;height:190px;background:var(--magenta);border-radius:34px 34px 0 34px;padding:26px 0 0 20px;font-family:"Bebas Neue",sans-serif;font-size:44px;line-height:45px;color:#fff}

  .photo{position:absolute}
  .photo-team{left:276px;top:42px;width:446px;height:311px;border-radius:0 0 60px 0;background:linear-gradient(160deg,#d8d2cf,#8e7f7a 55%,#5c6b3a)}
  .photo-class{left:38px;top:370px;width:207px;height:187px;border-radius:36px 0 36px 0;background:linear-gradient(150deg,#e4e0dc,var(--photo-people))}
  .photo-juice{left:38px;top:574px;width:207px;height:190px;border-radius:0 36px 0 36px;background:linear-gradient(135deg,#6f8a3a,var(--photo-juice) 45%,#f08a2e 70%,#6b1d35)}
  .photo-kitchen{left:38px;top:780px;width:207px;height:188px;border-radius:36px 0 36px 0;background:linear-gradient(160deg,#8a6a55,var(--photo-kitchen) 55%,#e8e2dc)}

  .content{position:absolute;left:278px;top:392px;width:425px;font-family:"Open Sans",sans-serif}
  .headline{font-family:"Bebas Neue",sans-serif;font-size:43px;line-height:44px;color:var(--magenta);white-space:nowrap}
  .intro{font-size:21px;line-height:31.5px;font-weight:600;color:var(--ink);margin-top:4px;white-space:nowrap}
  .focus-areas{font-size:21px;line-height:31.5px;font-weight:700;color:var(--magenta);white-space:nowrap}
  .services{list-style:none;margin-top:20px;padding-left:23px}
  .services li{position:relative;font-size:13.4px;line-height:19px;color:var(--ink);text-align:justify;margin-bottom:7.5px}
  .services li::before{content:"";position:absolute;left:-23px;top:5px;border-left:13px solid var(--magenta);border-top:5px solid transparent;border-bottom:5px solid transparent}
  .signature{font-size:33px;line-height:40px;font-weight:700;font-style:italic;color:var(--magenta);margin-top:2px;padding-left:3px}

  .footer{position:absolute;left:0;top:982px;width:812px;height:68px;background:var(--footer)}
  .footer-item{position:absolute;top:22px;display:flex;align-items:center;gap:8px;font-family:"Open Sans",sans-serif;font-size:14px;font-weight:700;color:#fff;white-space:nowrap}
  .footer-item svg{fill:var(--magenta)}
  .footer-sweep{position:absolute;left:0;top:0}
</style>
</head>
<body>
<main class="flyer">
  <svg class="side-sweep" viewBox="0 0 812 1050" aria-hidden="true">
    <path d="M738 0 Q790 330 776 660 Q762 930 706 990 L812 990 L812 0 Z" fill="var(--magenta)"/>
  </svg>

  <header class="brand">
    <div class="brand-row">
      <span class="brand-dot"></span>
      <div class="brand-name">Ardea Health<br>Consultants</div>
    </div>
    <p class="brand-tagline">Training &amp; Consulting</p>
  </header>

  <div class="pillars">KNOWLEDGE.<br>ANALYSIS.<br>STATISTICS.</div>

  <div class="photo photo-team" role="img" aria-label="Photo of a cheering group of professionals raising their arms"></div>
  <div class="photo photo-class" role="img" aria-label="Photo of a training class giving thumbs up around a table"></div>
  <div class="photo photo-juice" role="img" aria-label="Photo of fresh vegetable and fruit juices"></div>
  <div class="photo photo-kitchen" role="img" aria-label="Photo of a woman preparing a fresh salad in a kitchen"></div>

  <section class="content">
    <h1 class="headline">Health Consultants &amp; Groups</h1>
    <p class="intro">Innovative approaches to meeting the<br>5 year funding measures in the<br>content area of</p>
    <p class="focus-areas">Health, Nutrition, Oral Health &amp; Safety</p>
    <ul class="services">
      <li>Ardea Health Consultant has embarked on a new methodology designed to ensure programmes meet total requirments as prescribed under the <em>Health Service Programme</em>.</li>
      <li>Let us manage your health programme through remote and offsite measures to ensure total compliance and strategic methodology toward quality service approaches.</li>
      <li>Let us provide consultants to mentor your health manager nutrition content specialist facility/safety manager. These support consultants are advanced level academias in their specialised areas of focus.</li>
      <li>Let us provide Mock Reviews for your programme designed to assist management staff in Focus I, Focus II, review strategies for 2018.</li>
      <li>Let us provide T/TA for any new health nutrition, safety staff to ensure they are fully prepared to perform their job duties at their highest level of management approaches.</li>
    </ul>
    <p class="signature">Dana Morrow, CEO</p>
  </section>

  <footer class="footer">
    <svg class="footer-sweep" width="812" height="68" viewBox="0 0 812 68" aria-hidden="true">
      <path d="M706 0 Q690 40 666 68 L812 68 L812 0 Z" fill="var(--magenta)"/>
    </svg>
    <div class="footer-item" style="left:20px">
      <svg width="12" height="10" viewBox="0 0 12 10"><path d="M0 0h12v1.5L6 5.5 0 1.5Z"/><path d="M0 3l6 4 6-4v7H0Z"/></svg>
      <span>ardeahealthconsult@mail.com</span>
    </div>
    <div class="footer-item" style="left:280px">
      <svg width="13" height="13" viewBox="0 0 24 24"><path d="M6.6 10.8a15 15 0 0 0 6.6 6.6l2.2-2.2a1 1 0 0 1 1-.25 11.4 11.4 0 0 0 3.6.57 1 1 0 0 1 1 1V20a1 1 0 0 1-1 1A17 17 0 0 1 3 4a1 1 0 0 1 1-1h3.5a1 1 0 0 1 1 1c0 1.25.2 2.45.57 3.57a1 1 0 0 1-.25 1Z"/></svg>
      <span>(555) 014-2271</span>
    </div>
    <div class="footer-item" style="left:428px">
      <svg width="11" height="15" viewBox="0 0 24 32"><path d="M12 0A12 12 0 0 0 0 12c0 9 12 20 12 20s12-11 12-20A12 12 0 0 0 12 0Zm0 17a5 5 0 1 1 0-10 5 5 0 0 1 0 10Z"/></svg>
      <span>P.O. Box 4120 Maple Ridge, GA 30000</span>
    </div>
  </footer>
</main>
</body>
</html>
```